Wavelume artwork for new single release

I need Wavelume artwork creating to release a new single on there.

The specs are:

Ideal size: 3000 x 3000 pixels
Minimum size: 1400 x 1400 pixels
Aspect ratio: 1:1 (must be a perfect square)
File format: JPG or PNG
Color space: sRGB
File size: Max 4MB

The song is called "Still, Can We Wander?"
The artist is "Milo Fenwright"

We have no images of Milo, so it really is open to imagination.

Target Market(s)

Wavelume listeners

Industry/Entity Type

Music

```html
<!DOCTYPE html>
<html lang="en">
<head>
<meta charset="utf-8">
<title>Milo Fenwright – Still, Can We Wander?</title>
<link rel="stylesheet" href="https://fonts.googleapis.com/css2?family=Alfa+Slab+One&family=Courier+Prime:wght@700&family=Jost:wght@400&display=swap">
<style>
  :root {
    --cover-red: #ed2a26;
    --panel-white: #ffffff;
    --ink-black: #000000;
  }
  html, body {
    margin: 0;
    padding: 0;
    width: 1200px;
    height: 1200px;
    overflow: hidden;
    background: var(--cover-red);
  }
  .cover {
    position: relative;
    width: 1200px;
    height: 1200px;
    background: var(--cover-red);
  }
  .cover-art {
    position: absolute;
    inset: 0;
    width: 1200px;
    height: 1200px;
    display: block;
  }
  .title-panel { fill: var(--panel-white); }
  .artist-name {
    font-family: "Jost", "Futura", sans-serif;
    font-weight: 400;
    font-size: 90px;
  }
  .artist-name--shadow { fill: var(--ink-black); }
  .artist-name--main { fill: var(--cover-red); }
  .title-main {
    font-family: "Alfa Slab One", "American Typewriter", serif;
    font-size: 330px;
    fill: var(--ink-black);
  }
  .title-tail {
    font-family: "Courier Prime", "Courier New", monospace;
    font-weight: 700;
    font-size: 158px;
    fill: var(--ink-black);
  }
  .heart { fill: var(--cover-red); }
</style>
</head>
<body>
  <main class="cover">
    <svg class="cover-art" viewBox="0 0 1200 1200" xmlns="http://www.w3.org/2000/svg" aria-labelledby="cover-title">
      <title id="cover-title">Milo Fenwright – Still, Can We Wander?</title>

      <rect class="title-panel" x="278" y="193" width="841" height="949"/>

      <g class="artist">
        <text class="artist-name artist-name--shadow" x="305" y="296" textLength="770" lengthAdjust="spacing">MILO FENWRIGHT</text>
        <text class="artist-name artist-name--main" x="303" y="287" textLength="770" lengthAdjust="spacing">MILO FENWRIGHT</text>
      </g>

      <g class="song-title">
        <text class="title-main" x="300" y="655" textLength="780" lengthAdjust="spacingAndGlyphs">STILL,</text>
        <text class="title-main" x="300" y="950" textLength="262" lengthAdjust="spacingAndGlyphs">CAN</text>
        <path class="heart" d="M713 755 C693 731 667 724 650 724 C600 724 574 760 574 803 C574 875 672 937 713 960 C770 926 853 870 853 803 C853 758 819 724 777 724 C750 724 728 738 713 755 Z"/>
        <text class="title-main" x="866" y="950" textLength="214" lengthAdjust="spacingAndGlyphs">WE</text>
        <text class="title-tail" x="301" y="1084" textLength="777" lengthAdjust="spacingAndGlyphs">WANDER?</text>
      </g>
    </svg>
  </main>
</body>
</html>
```